Rancho Miralta - New Community in Seybaplaya
Affordable Country Lots in Campeche, Mexico
Rancho Miralta - New Community in Seybaplaya - Real Estate
Creative Brief
Real Estate
ranchomiralta.example
Not for profit company to promote affordable lots in Canada aiming at attracting soon to be retirees and young investors alike.
Company is family run and simple to operate and would like to portray such image.
New community is located 3kms from the beach in tropical weather year round.
Google images of seybaplaya and campeche to get a feel for local existing community.
We would like to show respect to the existing Spanish colonial architecture and heritage.
Likes, colorful, simple, easy to understand and to follow links to navigate within website, not too complicated to update Dislikes, complex, confusing, too plain or too colorful,
Must use existing logo: http://files.brandpixelhub.example/drafts/view/entry/804213/draft/7761904 Pages must fit in one screen and must be written in simple html coding to perform updates without engaging specialty programmers/designers.

```html
<!DOCTYPE html>
<html lang="en">
<head>
<meta charset="utf-8">
<title>Rancho Miralta – New Community in Seybaplaya</title>
<link href="https://fonts.googleapis.com/css2?family=Open+Sans:wght@400;600;700&display=swap" rel="stylesheet">
<style>
  :root {
    --bg: #dde9ec;
    --bg-deep: #c9dde2;
    --salmon: #f4ae93;
    --salmon-light: #f9d2c1;
    --salmon-dark: #e98f72;
    --teal: #17788a;
    --teal-dark: #0d5766;
    --teal-light: #2a97a8;
    --white: #ffffff;
    --nav-text: #ffffff;
  }
  * { margin: 0; padding: 0; box-sizing: border-box; }
  html, body { width: 1200px; height: 785px; overflow: hidden; }
  body {
    font-family: "Open Sans", Arial, sans-serif;
    background: var(--bg);
    position: relative;
  }
  .backdrop {
    position: absolute; inset: 0;
    background: radial-gradient(ellipse at 50% 45%, #eef5f6 0%, var(--bg) 55%, var(--bg-deep) 100%);
  }
  .top-band {
    position: absolute; left: 0; top: 0; width: 1200px; height: 96px;
    background: linear-gradient(to bottom, var(--salmon-dark) 0%, var(--salmon) 70%, var(--salmon-light) 100%);
  }
  .top-band::after {
    content: ""; position: absolute; left: 0; bottom: 0; width: 100%; height: 16px;
    background: #e6f0f2; opacity: .55;
  }
  .main-nav {
    position: absolute; top: 60px; left: 426px;
    display: flex; gap: 0;
  }
  .main-nav a {
    color: var(--nav-text); text-decoration: none;
    font-size: 16px; font-weight: 400; margin-right: 22px; position: relative;
  }
  .main-nav a.is-active::after {
    content: ""; position: absolute; left: 50%; top: 26px; margin-left: -7px;
    border-left: 7px solid transparent; border-right: 7px solid transparent;
    border-bottom: 8px solid var(--white);
  }
  .brand {
    position: absolute; left: 139px; top: -20px; width: 240px; height: 240px;
    border-radius: 50%; background: var(--white);
    border: 8px solid var(--salmon-light);
    display: flex; align-items: center; justify-content: center; z-index: 3;
  }
  .brand-name {
    font-weight: 700; color: var(--teal); font-size: 30px; line-height: 1.05;
    text-align: center; margin-top: 40px;
  }
  .stage {
    position: absolute; left: 144px; top: 120px; width: 929px; height: 516px;
    background: var(--white);
    box-shadow: 0 4px 14px rgba(40, 80, 90, .25);
  }
  .hero-photo {
    position: absolute; left: 19px; top: 19px; width: 886px; height: 365px;
    background: linear-gradient(to bottom, #6fb6e6 0%, #a9d6ef 38%, #2b87b6 48%, #1f6e9a 62%, #6eb4c8 76%, #e8d3b0 88%, #d9bf94 100%);
  }
  .slide-arrow {
    position: absolute; top: 453px; width: 38px; height: 38px;
    background: var(--teal-dark);
  }
  .slide-arrow.prev { left: 154px; }
  .slide-arrow.next { left: 1026px; }
  .slide-arrow svg { display: block; }
  .thumb-band {
    position: absolute; left: 0; top: 384px; width: 929px; height: 132px;
    background: linear-gradient(to bottom, var(--teal-light) 0%, var(--teal) 45%, var(--teal-dark) 100%);
  }
  .thumb-band .marker {
    position: absolute; left: 114px; top: 10px;
    border-left: 7px solid transparent; border-right: 7px solid transparent;
    border-bottom: 8px solid var(--white);
  }
  .thumbs {
    position: absolute; left: 43px; top: 29px; display: flex; gap: 58px;
  }
  .thumb {
    width: 166px; height: 103px; background: var(--white); padding: 6px 6px 0 6px; position: relative;
  }
  .thumb-image { width: 154px; height: 97px; }
  .thumb-label {
    position: absolute; left: 6px; bottom: 0; width: 154px; height: 28px;
    background: rgba(12, 80, 95, .85); color: var(--white);
    font-weight: 700; font-size: 17px; text-align: center; line-height: 28px; letter-spacing: .3px;
  }
  .floor {
    position: absolute; left: 144px; top: 636px; width: 929px; height: 36px;
  }
  .footer-rule {
    position: absolute; left: 144px; top: 674px; width: 929px; height: 3px; background: var(--teal-dark);
  }
  .copyright {
    position: absolute; left: 163px; top: 688px; font-size: 13px; color: var(--teal);
  }
</style>
</head>
<body>
  <div class="backdrop" role="img" aria-label="Soft backdrop of colonial arches"></div>
  <header class="top-band"></header>
  <nav class="main-nav">
    <a href="#">Location</a>
    <a href="#">Master Plan</a>
    <a href="#" class="is-active">Real Estate</a>
    <a href="#">Gallery</a>
    <a href="#">Our Company</a>
    <a href="#">Contact us</a>
  </nav>
  <div class="brand"><span class="brand-name">Rancho<br>Miralta</span></div>

  <main class="stage">
    <div class="hero-photo" role="img" aria-label="Seybaplaya beach at dusk with rocky shore, palms and a colourful house"></div>
    <section class="thumb-band">
      <span class="marker"></span>
      <div class="thumbs">
        <a class="thumb" href="#"><div class="thumb-image" role="img" aria-label="Palm silhouettes at sunset" style="background:linear-gradient(#e8a05a,#3a2a22)"></div><span class="thumb-label">SEYBAPLAYA</span></a>
        <a class="thumb" href="#"><div class="thumb-image" role="img" aria-label="Aerial view of community lots" style="background:linear-gradient(#8fae7a,#4d6e4a)"></div><span class="thumb-label">COMMUNITY</span></a>
        <a class="thumb" href="#"><div class="thumb-image" role="img" aria-label="Yellow colonial facade" style="background:linear-gradient(#e5c35e,#b98a3a)"></div><span class="thumb-label">ARCHITECTURE</span></a>
        <a class="thumb" href="#"><div class="thumb-image" role="img" aria-label="Golf green landscape" style="background:linear-gradient(#e7d6a6,#6f9a58)"></div><span class="thumb-label">LIFESTYLE</span></a>
      </div>
    </section>
  </main>

  <div class="slide-arrow prev"><svg width="38" height="38"><path d="M22 11 L14 19 L22 27" fill="none" stroke="#fff" stroke-width="4"/></svg></div>
  <div class="slide-arrow next"><svg width="38" height="38"><path d="M16 11 L24 19 L16 27" fill="none" stroke="#fff" stroke-width="4"/></svg></div>

  <svg class="floor" width="929" height="36" viewBox="0 0 929 36">
    <rect width="929" height="36" fill="#f4ae93"/>
    <polygon points="160,0 210,0 190,36 120,36" fill="#fde6dc"/>
    <polygon points="375,0 420,0 420,36 345,36" fill="#fde6dc"/>
    <polygon points="590,0 635,0 670,36 590,36" fill="#fde6dc"/>
    <polygon points="790,0 840,0 900,36 820,36" fill="#fde6dc"/>
  </svg>
  <div class="footer-rule"></div>
  <footer class="copyright">Copyright @ Rancho Miralta 2011</footer>
</body>
</html>
```